ReDesign Website for a more Bold approach

Hello! I'd like to redesign my website: torvellacapital.com

I'd like to add one thing that's not on my website which is a blog. The design around the blog should be put time into as I will be putting out incredibly great content and want it to attract viewers.

I get a lot of inspiration from quondel.com (the way they flow the big statements across each screen, colors)
amberlit.vc (the simplicity behind the design is beautiful)

I like modern very simple but bold approaches.

I am going to attach my logo here and if it can be thought of when making the design of the website. Thanks!

Industry/Entity Type

Finance and Private Equity

Number of Pages Required

3 page

Font styles to use
Serif
Sans Serif

Colors
0054AA
0677BA
7BADD7
CADEEF
E8F1F8
0094D4
00A9DD
6FCCEA
C7EBF8
E9F6FB
00AB8E
00BBA5
67D7C9
C6EFE9
E9F9F6

Requirements
Must have
• My project must have a Home, Expertise, Story, Clients, Approach, Blog, Contact
Nice to have
• It would be nice to have these tabs reduced to 1-3 pages
Should not have
• My project must not have bright colors.

```html
<!DOCTYPE html>
<html lang="en">
<head>
<meta charset="utf-8">
<title>Torvella Capital — Approach</title>
<link href="https://fonts.googleapis.com/css2?family=Spectral:wght@400&family=Poppins:wght@400;500;600;800&family=Raleway:wght@300&family=Montserrat:wght@600&display=swap" rel="stylesheet">
<style>
:root{
  --navy:#0b2540;
  --navy-foot:#0d2843;
  --accent:#0094d4;
  --accent-light:#6fccea;
  --tag-primary:#0054aa;
  --tag-secondary:#00ab8e;
  --ink:#111;
  --line:#333;
  --grey:#555;
  --white:#fff;
}
*{margin:0;padding:0;box-sizing:border-box}
html,body{width:702px;height:1200px;overflow:hidden}
body{position:relative;background:var(--white);font-family:"Poppins",sans-serif;color:var(--ink)}
.hero{position:absolute;left:0;top:0;width:702px;height:257px;background:var(--navy)}
.brand{position:absolute;font-family:"Montserrat",sans-serif;font-weight:600;font-size:11px;letter-spacing:.2px;color:var(--white);white-space:nowrap}
.nav{position:absolute;top:40px;right:69px;display:flex;gap:17px;font-size:8px;font-weight:500}
.nav a{color:var(--white);text-decoration:none}
.nav a.current{color:var(--accent-light)}
.hero-kicker{position:absolute;top:92px;width:100%;text-align:center;font-family:"Raleway",sans-serif;font-weight:300;font-size:35px;color:var(--accent-light)}
.hero-title{position:absolute;top:124px;width:100%;text-align:center;font-family:"Spectral",serif;font-weight:400;font-size:58px;color:var(--white)}
.expertise{position:absolute;left:0;top:257px;width:702px;height:688px}
.sec-kicker{position:absolute;top:66px;width:100%;text-align:center;font-family:"Raleway",sans-serif;font-weight:300;font-size:25px;color:var(--accent)}
.sec-title{position:absolute;top:86px;width:100%;text-align:center;font-family:"Spectral",serif;font-weight:400;font-size:32px}
.sec-intro{position:absolute;top:134px;left:176px;width:350px;text-align:center;font-size:7.4px;line-height:12px;color:var(--grey)}
.timeline{position:absolute;left:0;top:0}
.pillar{position:absolute;width:218px}
.pillar h3{font-family:"Spectral",serif;font-weight:400;font-size:15.5px;margin-bottom:4px}
.pillar p{font-size:6px;line-height:9px;color:var(--grey)}
.pillar.right-side{text-align:right}
.footer{position:absolute;left:0;top:945px;width:702px;height:255px;background:var(--navy-foot);border-top:1.5px solid var(--accent);color:var(--white)}
.foot-blurb{position:absolute;left:82px;top:103px;width:160px;font-size:7.4px;line-height:12px}
.copyright{position:absolute;left:82px;top:157px;font-size:7px}
.copyright span{color:var(--accent-light)}
.foot-head{position:absolute;top:55px;font-family:"Spectral",serif;font-weight:400;font-size:15.5px}
.foot-links{position:absolute;left:293px;top:97px;list-style:none;font-size:7.4px;font-weight:500;line-height:16px}
.foot-links .current{color:var(--accent-light)}
.address{position:absolute;left:408px;top:98px;font-size:14px;font-weight:600;white-space:nowrap}
.contact-line{position:absolute;left:407px;top:133px;display:flex;align-items:center;font-size:8.5px;font-weight:600}
.contact-line .sep{width:1px;height:12px;background:var(--white);margin:0 11px}
.contact-line .mail{color:var(--accent-light);font-weight:500}
.socials{position:absolute;left:405px;top:165px;display:flex;gap:5px}
.socials span{width:19px;height:19px;border-radius:50%;background:var(--white)}
</style>
</head>
<body>
<header class="hero">
  <div class="brand" style="left:69px;top:38px">TORVELLA CAPITAL</div>
  <nav class="nav">
    <a href="#">Home</a><a class="current" href="#">Approach</a><a href="#">About us</a><a href="#">Blog</a><a href="#">Contact</a>
  </nav>
  <div class="hero-kicker">Here's Our</div>
  <h1 class="hero-title">Approach</h1>
</header>

<section class="expertise">
  <div class="sec-kicker">Our</div>
  <h2 class="sec-title">Expertise</h2>
  <p class="sec-intro">We've built our approach to helping your startup thrive based around three key developmental pillars that guarantee results for our partners.</p>

  <svg class="timeline" width="702" height="688" viewBox="0 0 702 688">
    <path d="M326 208 C326 262 373 262 373 305 C373 355 326 358 326 407 C326 457 373 460 373 506 C373 556 326 560 326 610" fill="none" stroke="var(--line)" stroke-width="2.5" stroke-linecap="round"/>
    <path d="M236 265 H291 L325 299 Q328 303.5 325 308 L291 342 H236 Q230 342 230 336 V271 Q230 265 236 265Z" fill="var(--tag-primary)"/>
    <path d="M462 369 H408 L375 402 Q372 407.5 375 412 L408 446 H462 Q468 446 468 440 V375 Q468 369 462 369Z" fill="var(--tag-secondary)"/>
    <path d="M236 468 H291 L325 502 Q328 506.5 325 511 L291 545 H236 Q230 545 230 539 V474 Q230 468 236 468Z" fill="var(--tag-primary)"/>
    <g fill="var(--line)">
      <circle cx="344" cy="305" r="1.6"/><circle cx="351" cy="305" r="1.6"/><circle cx="358" cy="305" r="1.6"/>
      <circle cx="342" cy="407" r="1.6"/><circle cx="349" cy="407" r="1.6"/><circle cx="356" cy="407" r="1.6"/>
      <circle cx="344" cy="506" r="1.6"/><circle cx="351" cy="506" r="1.6"/><circle cx="358" cy="506" r="1.6"/>
    </g>
    <circle cx="373" cy="305" r="8.5" fill="var(--tag-primary)" stroke="var(--line)" stroke-width="3"/>
    <circle cx="326" cy="407" r="8.5" fill="var(--tag-secondary)" stroke="var(--line)" stroke-width="3"/>
    <circle cx="373" cy="506" r="8.5" fill="var(--tag-primary)" stroke="var(--line)" stroke-width="3"/>
    <g font-family="Poppins, sans-serif" font-weight="800" font-size="33" fill="var(--white)" text-anchor="middle">
      <text x="271" y="316">1</text>
      <text x="429" y="419">2</text>
      <text x="270" y="519">3</text>
    </g>
  </svg>

  <div class="pillar" style="left:408px;top:270px">
    <h3>Expertise</h3>
    <p>We've built our firm on a bank of insights, knowledge and proficiencies honed over years of working with the biggest names in venture capitalism – that experience forms the backbone of every project, every pitch and every investment.</p>
  </div>
  <div class="pillar right-side" style="left:75px;top:377px">
    <h3>Collaboration</h3>
    <p>We believe that the best partnerships start with a combined and cooperative approach that benefits all parties every step of the way. We'll always keep our partners up-to-date with our work using regular touchpoints and reports.</p>
  </div>
  <div class="pillar" style="left:408px;top:481px;width:208px">
    <h3>Trust</h3>
    <p>We know that our clients and our partners know their industry better than we do, so we trust their input and their ideas – pairing them up with our own business intelligence to guarantee success.</p>
  </div>
</section>

<footer class="footer">
  <div class="brand" style="left:82px;top:64px">TORVELLA CAPITAL</div>
  <p class="foot-blurb">Pellentesque habitant morbi tristique senectus et netus et malesuada fames ac turpis egestas.</p>
  <p class="copyright">© 2022 <span>TORVELLACAPITAL.COM</span></p>
  <h4 class="foot-head" style="left:293px">Pages</h4>
  <ul class="foot-links">
    <li>Home</li><li class="current">Approach</li><li>About us</li><li>Blog</li><li>Contact</li>
  </ul>
  <h4 class="foot-head" style="left:407px">Contact Details</h4>
  <div class="address">18 Harrowmere, Castleford England</div>
  <div class="contact-line">
    <svg width="14" height="14" viewBox="0 0 24 24" fill="none" stroke="var(--accent-light)" stroke-width="1.6" stroke-linejoin="round" aria-hidden="true"><path d="M5 3h4l2 5-2.5 1.5a11 11 0 0 0 6 6L16 13l5 2v4a2 2 0 0 1-2 2A16 16 0 0 1 3 5a2 2 0 0 1 2-2z"/></svg>
    <span style="margin-left:6px">+44-7720418353</span>
    <span class="sep"></span>
    <span class="mail">hello@torvellacapital.com</span>
  </div>
  <div class="socials" aria-label="Social links"><span></span><span></span><span></span><span></span></div>
</footer>
</body>
</html>
```